Business card design for engineering firm specializing in defense industry.

We need a professional business card design. Something simple but stands out. We are an engineering company specializing in composites in the defense industry.
Industry/Entity Type
Defense
Contact Information for Business Card
A simple black business card with the Varlonix yellow color is what we had in mind but open for other designs.
Colors
ffc214

```html
<!DOCTYPE html>
<html lang="en">
<head>
<meta charset="utf-8">
<title>Varlonix Business Card</title>
<link href="https://fonts.googleapis.com/css2?family=Oswald:wght@400;500;600&display=swap" rel="stylesheet">
<style>
  :root {
    --page-bg: #f5f5f5;
    --card-dark: #241f20;
    --card-light: #ffffff;
    --brand-yellow: #ffc214;
    --ink: #2b2b2b;
    --ink-soft: #3a3a3a;
    --mark-grey: #5a5758;
    --mark-dark: #141213;
  }
  * { box-sizing: border-box; margin: 0; padding: 0; }
  html, body {
    width: 1200px; height: 900px; overflow: hidden;
    background: var(--page-bg);
    font-family: "Oswald", "Arial Narrow", sans-serif;
  }
  .canvas { position: relative; width: 1200px; height: 900px; }

  .card { position: absolute; width: 590px; height: 336px; }
  .card--back { left: 305px; top: 97px; background: var(--card-dark); }
  .card--front { left: 305px; top: 464px; background: var(--card-light); }

  /* Back side */
  .back-wordmark {
    position: absolute; left: 48px; top: 140px;
    font-size: 40px; font-weight: 600; letter-spacing: 1px;
    color: var(--mark-grey); line-height: 1;
  }
  .back-block {
    position: absolute; left: 360px; top: 108px;
    width: 120px; height: 120px; background: var(--mark-dark);
  }

  /* Front side */
  .brand {
    position: absolute; left: 33px; top: 58px;
    display: flex; align-items: center; gap: 14px;
  }
  .brand__square { width: 40px; height: 40px; background: var(--brand-yellow); }
  .brand__name {
    font-size: 40px; font-weight: 600; letter-spacing: 1px;
    color: var(--ink); line-height: 1;
  }

  .person { position: absolute; right: 34px; top: 144px; text-align: right; }
  .person__name { font-size: 28px; font-weight: 500; color: var(--ink); line-height: 1.1; }
  .person__role { font-size: 14px; font-weight: 400; color: var(--brand-yellow); margin-top: 2px; }

  .divider {
    position: absolute; left: 33px; right: 35px; top: 211px;
    height: 2px; background: var(--brand-yellow);
  }

  .contacts { position: absolute; left: 33px; top: 230px; list-style: none; }
  .contacts li {
    display: flex; align-items: center; gap: 11px;
    height: 24px; font-size: 16px; color: var(--ink-soft);
  }
  .icon { width: 18px; height: 18px; flex: none; }

  .address {
    position: absolute; right: 34px; top: 230px;
    display: flex; gap: 8px; align-items: flex-start;
  }
  .address__lines { text-align: right; font-size: 16px; color: var(--ink-soft); line-height: 24px; }
  .address .icon { margin-top: 3px; }
</style>
</head>
<body>
<main class="canvas">
  <section class="card card--back" aria-label="Card back">
    <div class="back-wordmark">Varlonix</div>
    <div class="back-block"></div>
  </section>

  <section class="card card--front" aria-label="Card front">
    <div class="brand">
      <span class="brand__square"></span>
      <span class="brand__name">Varlonix</span>
    </div>

    <div class="person">
      <div class="person__name">Daniel Whitford</div>
      <div class="person__role">President &amp; CEO</div>
    </div>

    <div class="divider"></div>

    <ul class="contacts">
      <li>
        <svg class="icon" viewBox="0 0 24 24" aria-hidden="true"><path fill="#ffc214" d="M6.6 10.8a15.1 15.1 0 0 0 6.6 6.6l2.2-2.2c.3-.3.7-.4 1-.2 1.1.4 2.3.6 3.6.6.6 0 1 .4 1 1V20c0 .6-.4 1-1 1A17 17 0 0 1 3 4c0-.6.4-1 1-1h3.5c.6 0 1 .4 1 1 0 1.3.2 2.5.6 3.6.1.3 0 .7-.2 1z"/></svg>
        <span>0475 214 390</span>
      </li>
      <li>
        <svg class="icon" viewBox="0 0 24 24" aria-hidden="true"><rect x="2" y="5" width="20" height="14" fill="#ffc214"/><path d="M2 5l10 8 10-8" fill="none" stroke="#fff" stroke-width="1.6"/></svg>
        <span>info@varlonix-eng.com</span>
      </li>
      <li>
        <svg class="icon" viewBox="0 0 24 24" aria-hidden="true"><circle cx="12" cy="12" r="10" fill="#ffc214"/><path d="M2 12h20M12 2c3 3 3 17 0 20M12 2c-3 3-3 17 0 20" fill="none" stroke="#fff" stroke-width="1.4"/></svg>
        <span>www.varlonix-eng.com</span>
      </li>
    </ul>

    <div class="address">
      <div class="address__lines">
        <div>418 Harlow Ridge Road, Brenton Falls</div>
        <div>27590, North Carolina</div>
      </div>
      <svg class="icon" viewBox="0 0 24 24" aria-hidden="true"><path fill="#ffc214" d="M12 2a7 7 0 0 0-7 7c0 5 7 13 7 13s7-8 7-13a7 7 0 0 0-7-7zm0 9.5A2.5 2.5 0 1 1 12 6.5a2.5 2.5 0 0 1 0 5z"/></svg>
    </div>
  </section>
</main>
</body>
</html>
```